Generative AI radar Infographics

I want to create an infographic called "Machine Learning Prospect Compass for Tender Replies". (see slide 3 of the PowerPoint file). I want to use it on social media (ConnectHub and Website). I added 2 inspiration graphics in my brief (see slide 2 of the PowerPoint). I want to add my logo on the infographic. (I also uploaded my company logos). You can find model detailed instructions on slide 1 of the PowerPoint.
Business development and sales
I am a business consultant. I will be using this infographics on Connecthub and in my powerpoint presentations to clients

```html
<!DOCTYPE html>
<html lang="en">
<head>
<meta charset="utf-8">
<title>Machine Learning Prospect Compass for Tender Replies</title>
<link href="https://fonts.googleapis.com/css2?family=Montserrat:wght@400;500;600;700&display=swap" rel="stylesheet">
<style>
  :root {
    --bg: #0a2c3e;
    --accent: #0b93b8;
    --band-grey: #c9cacc;
    --ink-dark: #0a2c3e;
    --white: #ffffff;
    --ring: rgba(160, 220, 240, 0.28);
    --dot-core: #d9f6ff;
    --dot-glow: #4fd0ff;
  }
  html, body { margin: 0; padding: 0; width: 1200px; height: 1200px; overflow: hidden; background: var(--bg); }
  .compass { display: block; width: 1200px; height: 1200px; font-family: 'Montserrat', sans-serif; }
  .title { font-weight: 600; font-size: 74px; letter-spacing: 3px; fill: var(--white); }
  .title .highlight { fill: var(--accent); }
  .axis-heading { font-weight: 700; font-size: 29px; fill: var(--white); letter-spacing: 0.5px; }
  .axis-sub { font-weight: 400; font-size: 31px; fill: var(--white); letter-spacing: 0.5px; }
  .band-label { font-weight: 600; font-size: 46px; letter-spacing: 5px; }
  .band-label.on-grey { fill: var(--ink-dark); }
  .band-label.on-blue { fill: var(--white); }
  .item { font-weight: 400; font-size: 19px; fill: var(--white); letter-spacing: 0.3px; }
  .guide-arc { fill: none; stroke: var(--accent); stroke-width: 3; }
  .guide-node { fill: var(--accent); }
  .ring { fill: none; stroke: var(--ring); stroke-width: 1.3; }
  .axis-line { stroke: rgba(120, 220, 255, 0.55); stroke-width: 2; }
  .site { font-weight: 700; font-size: 31px; fill: var(--white); letter-spacing: 1px; }
  .brand { font-weight: 600; font-size: 46px; fill: var(--white); letter-spacing: 2px; }
</style>
</head>
<body>
<svg class="compass" viewBox="0 0 1932 1932" xmlns="http://www.w3.org/2000/svg" role="img" aria-label="Machine Learning Prospect Compass for Tender Replies">
  <defs>
    <linearGradient id="fill-decision" x1="534" y1="0" x2="964" y2="0" gradientUnits="userSpaceOnUse">
      <stop offset="0" stop-color="#2a8a2c"/>
      <stop offset="1" stop-color="#12333a"/>
    </linearGradient>
    <linearGradient id="fill-development" x1="964" y1="0" x2="1394" y2="0" gradientUnits="userSpaceOnUse">
      <stop offset="0" stop-color="#0d5877"/>
      <stop offset="1" stop-color="#0b3148"/>
    </linearGradient>
    <linearGradient id="fill-capture" x1="534" y1="0" x2="964" y2="0" gradientUnits="userSpaceOnUse">
      <stop offset="0" stop-color="#0b2c40"/>
      <stop offset="0.45" stop-color="#1e2f5e"/>
      <stop offset="1" stop-color="#2a3878"/>
    </linearGradient>
    <linearGradient id="fill-strategy" x1="964" y1="0" x2="1394" y2="0" gradientUnits="userSpaceOnUse">
      <stop offset="0" stop-color="#0b2c40"/>
      <stop offset="1" stop-color="#6a3a4c"/>
    </linearGradient>
    <radialGradient id="dot-fill">
      <stop offset="0" stop-color="#ffffff"/>
      <stop offset="0.45" stop-color="var(--dot-core)"/>
      <stop offset="1" stop-color="var(--dot-glow)"/>
    </radialGradient>
    <filter id="glow" x="-100%" y="-100%" width="300%" height="300%">
      <feGaussianBlur stdDeviation="4" result="b"/>
      <feMerge><feMergeNode in="b"/><feMergeNode in="SourceGraphic"/></feMerge>
    </filter>
    <symbol id="marker" viewBox="-16 -16 32 32" overflow="visible">
      <circle r="11" fill="#0a2c3e" stroke="#5ad2ff" stroke-width="2" filter="url(#glow)"/>
      <circle r="6" fill="url(#dot-fill)"/>
    </symbol>
    <path id="arc-decision" d="M 486 1034 A 478 478 0 0 1 964 556"/>
    <path id="arc-development" d="M 964 556 A 478 478 0 0 1 1442 1034"/>
    <path id="arc-capture" d="M 444 1034 A 520 520 0 0 0 964 1554"/>
    <path id="arc-strategy" d="M 964 1554 A 520 520 0 0 0 1484 1034"/>
  </defs>

  <rect class="backdrop" width="1932" height="1932" fill="var(--bg)"/>

  <!-- Title -->
  <text class="title" x="966" y="155" text-anchor="middle"><tspan class="highlight">MACHINE LEARNING</tspan> PROSPECT</text>
  <text class="title" x="966" y="243" text-anchor="middle">COMPASS FOR TENDER REPLIES</text>

  <!-- Outer guide arcs -->
  <g class="guides">
    <path class="guide-arc" d="M 821 416 A 634 634 0 0 0 346 891"/>
    <path class="guide-arc" d="M 1107 416 A 634 634 0 0 1 1582 891"/>
    <path class="guide-arc" d="M 346 1177 A 634 634 0 0 0 821 1652"/>
    <path class="guide-arc" d="M 1107 1652 A 634 634 0 0 0 1582 1177"/>
    <circle class="guide-node" cx="821" cy="416" r="14"/>
    <circle class="guide-node" cx="1107" cy="416" r="14"/>
    <circle class="guide-node" cx="346" cy="891" r="14"/>
    <circle class="guide-node" cx="1582" cy="891" r="14"/>
    <circle class="guide-node" cx="346" cy="1177" r="14"/>
    <circle class="guide-node" cx="1582" cy="1177" r="14"/>
    <circle class="guide-node" cx="821" cy="1652" r="14"/>
    <circle class="guide-node" cx="1107" cy="1652" r="14"/>
  </g>

  <!-- Axis labels -->
  <text class="axis-heading" x="964" y="385" text-anchor="middle">PROCESS</text>
  <text class="axis-sub" x="964" y="420" text-anchor="middle">enhancement</text>
  <text class="axis-heading" x="964" y="1702" text-anchor="middle">STRATEGY</text>
  <text class="axis-sub" x="964" y="1737" text-anchor="middle">Enablement</text>
  <text class="axis-heading" x="359" y="993" text-anchor="end">INSIGHTS</text>
  <text class="axis-heading" x="359" y="1028" text-anchor="end">GENERATION</text>
  <text class="axis-sub" x="359" y="1063" text-anchor="end">(Transformative</text>
  <text class="axis-sub" x="359" y="1098" text-anchor="end">application)</text>
  <text class="axis-heading" x="1571" y="1010">TASK</text>
  <text class="axis-heading" x="1571" y="1045">AUTOMATION</text>
  <text class="axis-sub" x="1571" y="1080">(foundational use)</text>
  <use href="#marker" x="1866" y="1152" width="32" height="32"/>

  <!-- Outer quadrant bands -->
  <g class="bands">
    <path fill="var(--band-grey)" d="M 424 1022 A 540 540 0 0 1 952 494 L 952 576 A 458 458 0 0 0 506 1022 Z"/>
    <path fill="var(--accent)" d="M 976 494 A 540 540 0 0 1 1504 1022 L 1422 1022 A 458 458 0 0 0 976 576 Z"/>
    <path fill="var(--band-grey)" d="M 1504 1046 A 540 540 0 0 1 976 1574 L 976 1492 A 458 458 0 0 0 1422 1046 Z"/>
    <path fill="var(--accent)" d="M 952 1574 A 540 540 0 0 1 424 1046 L 506 1046 A 458 458 0 0 0 952 1492 Z"/>
    <text class="band-label on-grey"><textPath href="#arc-decision" startOffset="50%" text-anchor="middle">DECISION SUPPORT</textPath></text>
    <text class="band-label on-blue"><textPath href="#arc-development" startOffset="50%" text-anchor="middle">PROPOSAL DEVELOPMENT</textPath></text>
    <text class="band-label on-blue"><textPath href="#arc-capture" startOffset="50%" text-anchor="middle">CAPTURE STRATEGY</textPath></text>
    <text class="band-label on-grey"><textPath href="#arc-strategy" startOffset="50%" text-anchor="middle">PROPOSAL STRATEGY</textPath></text>
  </g>

  <!-- Radar quadrants -->
  <g class="radar">
    <path fill="url(#fill-decision)" d="M 964 1034 L 534 1034 A 430 430 0 0 1 964 604 Z"/>
    <path fill="url(#fill-development)" d="M 964 1034 L 964 604 A 430 430 0 0 1 1394 1034 Z"/>
    <path fill="url(#fill-strategy)" d="M 964 1034 L 1394 1034 A 430 430 0 0 1 964 1464 Z"/>
    <path fill="url(#fill-capture)" d="M 964 1034 L 964 1464 A 430 430 0 0 1 534 1034 Z"/>
    <circle class="ring" cx="964" cy="1034" r="143"/>
    <circle class="ring" cx="964" cy="1034" r="215"/>
    <circle class="ring" cx="964" cy="1034" r="287"/>
    <circle class="ring" cx="964" cy="1034" r="358"/>
    <circle class="ring" cx="964" cy="1034" r="430"/>
    <line class="axis-line" x1="964" y1="604" x2="964" y2="1464"/>
    <line class="axis-line" x1="534" y1="1034" x2="1394" y2="1034"/>
    <path fill="#5cff1a" d="M 964 1034 L 892 1034 A 72 72 0 0 1 964 962 Z"/>
    <path fill="#0d93b8" d="M 964 1034 L 964 962 A 72 72 0 0 1 1036 1034 Z"/>
    <path fill="#e85a68" d="M 964 1034 L 1036 1034 A 72 72 0 0 1 964 1106 Z"/>
    <path fill="#6644b8" d="M 964 1034 L 964 1106 A 72 72 0 0 1 892 1034 Z"/>
  </g>

  <!-- Decision support items -->
  <g class="items decision">
    <use href="#marker" x="740" y="640" width="32" height="32"/>
    <text class="item" x="787" y="652">Bid</text><text class="item" x="787" y="671">Qualification</text>
    <text class="item" x="858" y="753" text-anchor="end">Compliance</text><text class="item" x="858" y="772" text-anchor="end">assessment</text>
    <use href="#marker" x="873" y="742" width="32" height="32"/>
    <text class="item" x="744" y="821" text-anchor="end">Strategic Pricing</text><text class="item" x="744" y="840" text-anchor="end">optimization</text>
    <use href="#marker" x="752" y="810" width="32" height="32"/>
    <use href="#marker" x="542" y="878" width="32" height="32"/>
    <text class="item" x="589" y="890">Opportunity</text><text class="item" x="589" y="909">assessment</text>
    <text class="item" x="892" y="894" text-anchor="end">Win Probability</text><text class="item" x="892" y="913" text-anchor="end">modeling</text>
    <use href="#marker" x="905" y="883" width="32" height="32"/>
    <use href="#marker" x="596" y="946" width="32" height="32"/>
    <text class="item" x="640" y="958">Bid/No Bid</text><text class="item" x="640" y="977">Analysis</text>
  </g>

  <!-- Proposal development items -->
  <g class="items development">
    <text class="item" x="1139" y="652" text-anchor="end">CV and</text><text class="item" x="1143" y="671" text-anchor="end">Resumes</text>
    <use href="#marker" x="1155" y="640" width="32" height="32"/>
    <text class="item" x="1125" y="733" text-anchor="end">Company profile</text>
    <use href="#marker" x="1131" y="711" width="32" height="32"/>
    <text class="item" x="987" y="783">Technical</text><text class="item" x="987" y="802">solution</text>
    <text class="item" x="1197" y="779" text-anchor="end">CV and</text><text class="item" x="1201" y="798" text-anchor="end">Resumes</text>
    <use href="#marker" x="1209" y="768" width="32" height="32"/>
    <use href="#marker" x="1044" y="826" width="32" height="32"/>
    <text class="item" x="1091" y="838">Compliance</text><text class="item" x="1091" y="857">Matrix</text>
    <use href="#marker" x="1179" y="848" width="32" height="32"/>
    <text class="item" x="1214" y="860">Executive</text><text class="item" x="1214" y="879">Summary</text>
    <use href="#marker" x="1013" y="894" width="32" height="32"/>
    <text class="item" x="1051" y="906">Security</text><text class="item" x="1051" y="925">Questionnaires</text>
    <text class="item" x="1359" y="918" text-anchor="end">Due Diligence</text><text class="item" x="1359" y="937" text-anchor="end">Questionnaires</text>
    <use href="#marker" x="1365" y="906" width="32" height="32"/>
    <text class="item" x="1230" y="988" text-anchor="end">Statement</text><text class="item" x="1230" y="1007" text-anchor="end">of Work</text>
    <use href="#marker" x="1236" y="976" width="32" height="32"/>
  </g>

  <!-- Proposal strategy items -->
  <g class="items strategy">
    <use href="#marker" x="1081" y="1076" width="32" height="32"/>
    <text class="item" x="1119" y="1098">Proposal plan</text>
    <text class="item" x="1358" y="1141" text-anchor="end">Differentiators</text>
    <use href="#marker" x="1368" y="1118" width="32" height="32"/>
    <text class="item" x="1192" y="1184" text-anchor="end">Proposal outline</text>
    <use href="#marker" x="1197" y="1162" width="32" height="32"/>
    <use href="#marker" x="1089" y="1265" width="32" height="32"/>
    <text class="item" x="1136" y="1277">Win Theme</text><text class="item" x="1136" y="1296">extraction</text>
    <use href="#marker" x="1016" y="1370" width="32" height="32"/>
    <text class="item" x="1057" y="1382">Key messages</text><text class="item" x="1057" y="1401">extraction</text>
  </g>

  <!-- Capture strategy items -->
  <g class="items capture">
    <text class="item" x="818" y="1098" text-anchor="end">SWOT Analysis</text>
    <use href="#marker" x="820" y="1076" width="32" height="32"/>
    <use href="#marker" x="608" y="1136" width="32" height="32"/>
    <text class="item" x="648" y="1158">Capture Plan</text>
    <text class="item" x="818" y="1217" text-anchor="end">Customer Hot Buttons</text>
    <use href="#marker" x="822" y="1195" width="32" height="32"/>
    <use href="#marker" x="751" y="1227" width="32" height="32"/>
    <text class="item" x="770" y="1277" text-anchor="middle">Customer Intelligence</text>
    <use href="#marker" x="633" y="1314" width="32" height="32"/>
    <text class="item" x="674" y="1336">Competitive Intelligence</text>
    <use href="#marker" x="831" y="1359" width="32" height="32"/>
    <text class="item" x="848" y="1407" text-anchor="middle">Value Proposition</text>
  </g>

  <!-- Footer -->
  <text class="site" x="103" y="1831">WWW.CORVANTA.COM</text>
  <text class="brand" x="1830" y="1800" text-anchor="end">Corvanta Advisory Group</text>
</svg>
</body>
</html>
```